Re-Design an adult education portal

I need support to re-design an adult education portal. Currently the customer has an incomplete website which should be prepared in a new format.
I have the idea how to realize, but I have no clue how to design it. The hard thing is to have a "beautiful" website with available logo and main color. I hope you can support me.

Name of Website: tovelu (tovelu.example)
Content: adult eduction for adult in safety at work, mountain climbing, dog school. various courses in different areas. But on old webpage is hard to find the different possibilities.
main color: Ral 6011 (green) -> #6C7C59
logo: you see on top of website the logo (2 dogs and a mountain with a colour gradient).

new website: for new webpage I decided to have a navigation for each section of education. In the main area I would like to have some pictures to give an idea what content is behind. At the moment it looks terrible, so I decided to use you as support for me to make the webpage prettier :). And maybe you have an better idea how to make it great. -> current state of new web page: https://tovelu.brisk-host.example/

Target Market(s)

adult eduction for adult in safety at work, mountain climbing, dog school

Number of Pages Required

1 page

Font styles to use
Serif
Sans Serif

Requirements
Must have
• As main color is set "Ral 6011" (green) -> #6C7C59

```html
<!DOCTYPE html>
<html lang="de">
<head>
<meta charset="utf-8">
<title>tovelu – Ihr Ausbildungs- und Kurspartner</title>
<link href="https://fonts.googleapis.com/css2?family=Montserrat:wght@500;600;700;800&family=Open+Sans:wght@400;600&display=swap" rel="stylesheet">
<style>
:root{
  --green:#6C7C59;
  --green-dark:#56654a;
  --ink:#222;
  --muted:#555;
  --grey-bg:#f1f0ee;
  --white:#fff;
}
*{box-sizing:border-box;margin:0;padding:0}
html,body{width:1200px;height:4240px;overflow:hidden}
body{font-family:"Open Sans",Arial,sans-serif;color:var(--ink);background:var(--white);font-size:16px;line-height:1.6}
h1,h2,h3,.nav a,.btn,.brand{font-family:"Montserrat",Arial,sans-serif}
.btn{display:inline-block;font-size:13px;font-weight:700;letter-spacing:.06em;text-transform:uppercase;padding:12px 26px;border:2px solid var(--green);color:var(--white);background:var(--green);text-decoration:none;white-space:nowrap}
.btn.light{background:var(--white);color:var(--green)}
.ph{display:block}

/* header */
.site-header{height:112px;display:flex;justify-content:space-between;align-items:center;padding:0 130px}
.brand{display:flex;align-items:center;gap:8px;font-weight:700;font-size:22px;color:var(--green);white-space:nowrap}
.brand .dot{width:12px;height:12px;background:var(--green);border-radius:50%}
.header-right{display:flex;flex-direction:column;align-items:flex-end;gap:12px}
.contacts{display:flex;gap:36px;font-size:13px}
.contact{display:flex;gap:8px;align-items:center;line-height:1.2}
.contact .ic{width:26px;height:26px;background:var(--green);display:flex;align-items:center;justify-content:center}
.contact small{display:block;color:var(--muted);font-size:11px}
.nav{display:flex;gap:24px;white-space:nowrap}
.nav a{font-size:12px;font-weight:700;color:var(--ink);text-decoration:none;text-transform:uppercase}

/* hero */
.hero{position:relative;height:588px;background:linear-gradient(100deg,#3a3d3c 0%,#6d6f6b 30%,#8f979c 55%,#4a5257 100%)}
.hero-copy{position:absolute;left:650px;top:110px;width:440px;color:var(--white)}
.hero-copy h1{font-size:34px;font-weight:800;line-height:1.25;text-transform:uppercase;margin-bottom:24px}
.hero-copy p{font-size:20px;font-weight:600;line-height:1.45;margin-bottom:32px}
.dots{position:absolute;bottom:24px;left:0;right:0;display:flex;justify-content:center;gap:10px}
.dots span{width:8px;height:8px;border-radius:50%;background:rgba(255,255,255,.5)}
.dots span:first-child{background:var(--white)}

/* safety */
.section-title{text-align:center;font-size:22px;font-weight:800;text-transform:uppercase;position:relative;padding-bottom:14px}
.section-title::after{content:"";position:absolute;left:50%;bottom:0;width:60px;height:3px;background:var(--green);transform:translateX(-50%)}
.safety{height:472px;padding-top:90px}
.cards{display:flex;gap:12px;justify-content:center;margin-top:38px}
.card{width:228px;text-align:center}
.card .ph{height:228px}
.card p{font-size:14px;font-weight:600;margin-top:12px;line-height:1.35}

/* first aid */
.first-aid{display:flex;height:428px}
.first-aid .ph{width:630px;height:100%}
.panel{flex:1;background:var(--green);color:var(--white);padding:70px 90px 0 50px}
.panel h2{font-size:24px;font-weight:800;text-transform:uppercase;margin-bottom:24px}
.panel p{font-size:15px;margin-bottom:30px;max-width:430px}

/* dog school */
.dog-school{background:var(--grey-bg);height:660px;padding-top:72px}
.dog-grid{display:flex;gap:60px;padding:0 130px;margin-top:60px}
.dog-copy{width:400px}
.dog-copy p{font-size:17px;margin-bottom:24px}
.course-list{list-style:none;display:flex;flex-direction:column;gap:12px}
.course-list li{background:var(--white);border:1px solid var(--green);display:flex;justify-content:space-between;align-items:center;padding:8px 14px;font-family:"Montserrat",sans-serif;font-size:11px;font-weight:700;text-transform:uppercase}
.course-list li::after{content:"›";color:var(--green);font-size:18px;line-height:1}
.dog-grid .ph{width:480px;height:460px}

/* czv */
.czv{height:580px;display:flex;align-items:center;gap:70px;padding:0 130px}
.czv .ph{width:400px;height:460px}
.czv-copy{width:400px}
.czv-copy h2,.about-copy h2{font-size:24px;font-weight:800;text-transform:uppercase;margin-bottom:22px}
.czv-copy p{font-size:17px;margin-bottom:28px;color:var(--ink)}

/* mountain */
.mountain{position:relative;height:552px;background:linear-gradient(160deg,#1c2128 0%,#394450 40%,#6f7a6a 70%,#8c8a65 100%);padding:110px 0 0 130px;color:var(--white)}
.mountain h2{font-size:30px;font-weight:800;text-transform:uppercase;margin-bottom:20px}
.mountain ul{list-style:none;display:flex;flex-direction:column;gap:14px;width:320px;margin-bottom:40px}
.mountain li{border:1px solid var(--white);padding:6px 14px;display:flex;justify-content:space-between;font-size:15px}
.mountain li::after{content:"›";font-size:18px;line-height:1}

/* about */
.about{height:468px;display:flex}
.about .ph{width:600px;height:100%}
.about-copy{padding:70px 130px 0 60px;flex:1}
.about-copy p{font-size:15px;margin-bottom:32px;max-width:400px}

/* footer */
.site-footer{background:var(--grey-bg);height:340px;display:flex;padding:70px 130px 0;gap:50px}
.foot-brand{width:260px;padding-top:10px}
.foot-col{width:200px}
.foot-col h3{font-size:13px;font-weight:800;text-transform:uppercase;margin-bottom:16px}
.foot-col ul{list-style:none;font-size:12px;line-height:1.7;text-transform:uppercase}
.foot-item{display:flex;gap:10px;align-items:center;font-size:12px;margin-bottom:12px;line-height:1.4}
.foot-item .ic{width:24px;height:24px;flex:none;background:var(--green);border-radius:50%;display:flex;align-items:center;justify-content:center}
.copyright{height:40px;text-align:center;font-size:11px;color:var(--muted);line-height:40px}
</style>
</head>
<body>

<header class="site-header">
  <div class="brand"><span class="dot"></span>tovelu.example</div>
  <div class="header-right">
    <div class="contacts">
      <div class="contact"><span class="ic"><svg width="14" height="14" viewBox="0 0 24 24" fill="none" stroke="#fff" stroke-width="2"><rect x="3" y="5" width="18" height="14"/><path d="M3 6l9 7 9-7"/></svg></span><div><small>Email</small>info@tovelu.example</div></div>
      <div class="contact"><span class="ic"><svg width="14" height="14" viewBox="0 0 24 24" fill="#fff"><path d="M6.6 10.8a15 15 0 006.6 6.6l2.2-2.2c.3-.3.7-.4 1-.2 1.1.4 2.3.6 3.6.6.6 0 1 .4 1 1V20c0 .6-.4 1-1 1A17 17 0 013 4c0-.6.4-1 1-1h3.5c.6 0 1 .4 1 1 0 1.3.2 2.5.6 3.6.1.3 0 .7-.2 1z"/></svg></span><div><small>Telefon</small>+41 79 000 12 34</div></div>
    </div>
    <nav class="nav"><a href="#">Arbeitssicherheit</a><a href="#">Erste Hilfe</a><a href="#">Hundeschule</a><a href="#">CZV</a><a href="#">Bergausbildung</a><a href="#">Tovelu</a></nav>
  </div>
</header>

<section class="hero" role="img" aria-label="Kletterer an einer Felswand über einem Bergtal">
  <div class="hero-copy">
    <h1>Ihr Ausbildungs-<br>und Kurspartner</h1>
    <p>Wir bieten Ihnen Wünschen entsprechende Ausbildungen, zielorientiert und Ihrem Können und Wissen angepasst.</p>
    <a class="btn" href="#">Weiterlesen</a>
  </div>
  <div class="dots"><span></span><span></span><span></span><span></span></div>
</section>

<section class="safety">
  <h2 class="section-title">Arbeitssicherheit</h2>
  <div class="cards">
    <div class="card"><div class="ph" role="img" aria-label="Stapler in einer Lagerhalle" style="background:linear-gradient(135deg,#c9cdd0,#e2a23a)"></div><p>Stapler</p></div>
    <div class="card"><div class="ph" role="img" aria-label="Persönliche Schutzausrüstung: Helm, Gehörschutz, Brille" style="background:linear-gradient(135deg,#f2f2f2,#e8c23a)"></div><p>Persönliche Schutzausrüstung gegen Absturz</p></div>
    <div class="card"><div class="ph" role="img" aria-label="Hubarbeitsbühne vor blauem Himmel" style="background:linear-gradient(160deg,#8fb8d8,#e4c04a)"></div><p>Hubarbeitsbühne</p></div>
    <div class="card"><div class="ph" role="img" aria-label="Arbeiter mit Helm bei der Materialkontrolle" style="background:linear-gradient(135deg,#d9dcdf,#b5bac0)"></div><p>Material Kontrolle</p></div>
  </div>
</section>

<section class="first-aid">
  <div class="ph" role="img" aria-label="Erste-Hilfe-Kurs mit Übungspuppe" style="background:linear-gradient(135deg,#8a8d8c,#c9b9a8 60%,#6e7680)"></div>
  <div class="panel">
    <h2>Erste Hilfe</h2>
    <p>Wir bieten Ihnen nach Ihren Wünschen angepasste Kurse im Sanitäts- und Rettungsbereich an. Firmenkurse werden auf Ihre Bedürfnisse und Gegebenheiten angepasst. Die Firma selbst ist nach KVR zertifiziert.</p>
    <a class="btn light" href="#">Weiterlesen</a>
  </div>
</section>

<section class="dog-school">
  <h2 class="section-title">Hundeschule</h2>
  <div class="dog-grid">
    <div class="dog-copy">
      <p>There are many variations of passages of Lorem Ipsum available, but the majority have suffered alteration in some form, by injected humour, or randomised words which don't look even slightly believable. If you are going to use a passage of Lorem Ipsum, you need to be sure there isn't anything</p>
      <ul class="course-list">
        <li>Theorie vor dem Hundekauf</li>
        <li>Welpenschule</li>
        <li>Obligatorische Kurse NHB</li>
        <li>Schnüffelausbildung</li>
        <li>Lawinenhundeausbildung</li>
      </ul>
    </div>
    <div class="ph" role="img" aria-label="Junger Hund vor einem Agility-Tunnel auf einer Wiese" style="background:linear-gradient(160deg,#6f9a45,#9cc24e 45%,#3f6e2a)"></div>
  </div>
</section>

<section class="czv">
  <div class="ph" role="img" aria-label="Roter Brandmelder an einer Wand" style="background:linear-gradient(135deg,#cfdbe6,#6f8fb0 55%,#b22a2a)"></div>
  <div class="czv-copy">
    <h2>CZV</h2>
    <p>There are many variations of passages of Lorem Ipsum available, but the majority have suffered alteration in some form, by injected humour, or randomised words which don't look even slightly believable. If you are going to use a passage of Lorem Ipsum, you need to be sure there isn't anything</p>
    <a class="btn" href="#">Weiterlesen</a>
  </div>
</section>

<section class="mountain" role="img" aria-label="Trailläuferin auf einem Berggrat über einem Tal">
  <h2>Bergausbildung</h2>
  <ul>
    <li>Grundausbildung Sommer</li>
    <li>Seiltechnik</li>
    <li>Lawinenkunde</li>
    <li>Alpine Rettung</li>
  </ul>
  <a class="btn" href="#">Weiterlesen</a>
</section>

<section class="about">
  <div class="ph" role="img" aria-label="Medizinische Übungspuppe mit Atemmaske" style="background:linear-gradient(90deg,#c7b8ad,#e6ddd6 70%,#fff)"></div>
  <div class="about-copy">
    <h2>Wir sind Tovelu,<br>eure Kurspartner</h2>
    <p>In meiner Beruflichen Laufbahn erlebte ich immer wieder Situationen, welche in mir die Idee reifen liessen, jedem interessierten Menschen ein Grundwissen zukommen zu lassen, welches ihn bei einer Notsituation richtig und mit der nötigen Ruhe reagieren lässt. Das Zusammenlegen &amp; Kombinieren von Wissen und Fertigkeiten der verschiedenen Fachbereiche gibt dem Menschen Sicherheit und Vertrauen in seinem Handeln.</p>
    <a class="btn" href="#">Weiterlesen</a>
  </div>
</section>

<footer class="site-footer">
  <div class="foot-brand"><div class="brand"><span class="dot"></span>tovelu.example</div></div>
  <div class="foot-col">
    <h3>Menü</h3>
    <ul><li>Arbeitssicherheit</li><li>Erste Hilfe</li><li>Hundeschule</li><li>CZV</li><li>Bergausbildung</li><li>Tovelu</li></ul>
  </div>
  <div class="foot-col">
    <h3>Contact us</h3>
    <div class="foot-item"><span class="ic"><svg width="12" height="12" viewBox="0 0 24 24" fill="#fff"><path d="M12 2a7 7 0 00-7 7c0 5 7 13 7 13s7-8 7-13a7 7 0 00-7-7zm0 9.5A2.5 2.5 0 1112 6.5a2.5 2.5 0 010 5z"/></svg></span>Musterweg 12<br>9000 Talhausen</div>
    <div class="foot-item"><span class="ic"><svg width="12" height="12" viewBox="0 0 24 24" fill="#fff"><path d="M6.6 10.8a15 15 0 006.6 6.6l2.2-2.2c.3-.3.7-.4 1-.2 1.1.4 2.3.6 3.6.6.6 0 1 .4 1 1V20c0 .6-.4 1-1 1A17 17 0 013 4c0-.6.4-1 1-1h3.5c.6 0 1 .4 1 1 0 1.3.2 2.5.6 3.6.1.3 0 .7-.2 1z"/></svg></span>Call us<br>+41 79 000 12 34</div>
    <div class="foot-item"><span class="ic"><svg width="12" height="12" viewBox="0 0 24 24" fill="none" stroke="#fff" stroke-width="2.5"><rect x="3" y="5" width="18" height="14"/><path d="M3 6l9 7 9-7"/></svg></span>E-mail us<br>info@tovelu.example</div>
  </div>
  <div class="foot-col">
    <h3>Follow us</h3>
    <div class="foot-item"><span class="ic"></span>Neuigkeiten<br>tovelu</div>
    <div class="foot-item"><span class="ic"></span>Kursfotos<br>tovelu</div>
    <div class="foot-item"><span class="ic"></span>Videos<br>tovelu</div>
  </div>
</footer>
<div class="copyright">Copyright © 2024. All Rights Reserved.</div>

</body>
</html>
```